Business card design needed

I need a business card that sets my business apart from big gyms and intimidating personal trainers. My personal training business focuses on outdoor and client in-home training, in an environment that is both enjoyable and sustainable for the client.
I train males and females, however a large proportion of my clientelle are female, so I would like the card to lean towards females, but still have a bit of masculine appeal about it.
My business colours are a deep sky blue and lightish red/orange (as seen in logo)

Contact Information for Business Card

Stride & Shine Coaching
Discover a happier, healthier you!
Benedict Rowlan- Health and Fitness Professional
Locations all across the Yarra Valley and Eastern Suburbs of Melbourne
0438152906
benedictrowlanpt@mailora.com.au

Requirements
Must have
• - Mobile number must stand out
- The 'Locations all across the Yarra Valley and Eastern Suburbs of Melbourne' must be clear and easy to read (different colour maybe?)

```html
<!DOCTYPE html>
<html lang="en">
<head>
<meta charset="utf-8">
<title>Benedict Rowlan – Business Card</title>
<link rel="stylesheet" href="https://fonts.googleapis.com/css2?family=PT+Sans:wght@400;700&family=Arimo:wght@400&display=swap">
<style>
  :root {
    --sky-blue: #1a78c2;
    --band-blue: #1b7bc4;
    --coral: #ef5a2a;
    --ink: #111111;
    --arc-blue: #c9ddee;
    --arc-fill: #f1f4f7;
    --card-white: #ffffff;
    --backdrop-light: #c4c8cd;
    --backdrop-dark: #7d838b;
  }
  * { margin: 0; padding: 0; box-sizing: border-box; }
  html, body { width: 1200px; height: 893px; overflow: hidden; }
  body {
    background: radial-gradient(ellipse at 50% 30%, var(--backdrop-light), var(--backdrop-dark));
    position: relative;
    font-family: "PT Sans", sans-serif;
  }
  .business-card {
    position: absolute;
    left: 180px; top: 206px;
    width: 840px; height: 480px;
    background: var(--card-white);
    overflow: hidden;
    box-shadow: 0 10px 30px rgba(0,0,0,0.25);
  }
  .card-arc { position: absolute; left: 0; top: 0; }
  .brand-lockup {
    position: absolute;
    left: 40px; top: 170px;
    width: 260px;
    display: flex; flex-direction: column; align-items: center; gap: 14px;
  }
  .brand-dot {
    width: 70px; height: 70px; border-radius: 50%;
    background: var(--coral);
  }
  .brand-name {
    color: var(--sky-blue);
    font-weight: 700; font-size: 24px; line-height: 1.1;
    text-align: center;
  }
  .contact-block { position: absolute; left: 330px; top: 92px; }
  .person-name { font-size: 36px; font-weight: 700; color: var(--ink); letter-spacing: 0.5px; }
  .person-role { font-size: 21px; color: var(--ink); margin-top: -2px; }
  .contact-line {
    display: flex; align-items: flex-start; gap: 10px;
    color: var(--sky-blue); font-weight: 700;
  }
  .contact-line svg { flex: none; margin-top: 4px; }
  .service-area { font-size: 23px; line-height: 1.05; margin-top: 26px; }
  .mobile-number { font-size: 25px; margin-top: 10px; letter-spacing: 0.5px; }
  .email-band {
    position: absolute; left: 0; bottom: 0;
    width: 100%; height: 92px;
    background: var(--band-blue);
    display: flex; align-items: center; justify-content: center;
  }
  .email-address {
    font-family: "Arimo", sans-serif;
    color: var(--card-white); font-size: 22px;
  }
</style>
</head>
<body>
  <main class="business-card">
    <svg class="card-arc" width="840" height="480" viewBox="0 0 840 480" aria-hidden="true">
      <circle cx="-60" cy="200" r="330" fill="var(--arc-fill)"/>
      <circle cx="-60" cy="200" r="336" fill="none" stroke="var(--arc-blue)" stroke-width="12"/>
    </svg>

    <div class="brand-lockup">
      <span class="brand-dot"></span>
      <span class="brand-name">Stride &amp; Shine Coaching</span>
    </div>

    <section class="contact-block">
      <h1 class="person-name">Benedict Rowlan</h1>
      <p class="person-role">Health and Fitness Professional</p>

      <p class="contact-line service-area">
        <svg width="18" height="18" viewBox="0 0 18 18" aria-hidden="true">
          <path d="M9 1 L17 8 H14.5 V17 H3.5 V8 H1 Z" fill="var(--coral)"/>
          <rect x="7" y="11" width="4" height="6" fill="#ffffff"/>
        </svg>
        <span>Locations all across the Yarra Valley and<br>Eastern Suburbs of Melbourne</span>
      </p>

      <p class="contact-line mobile-number">
        <svg width="14" height="20" viewBox="0 0 14 20" aria-hidden="true">
          <rect x="1" y="1" width="12" height="18" rx="2" fill="var(--coral)"/>
          <rect x="3" y="3.5" width="8" height="11" fill="#ffffff"/>
          <circle cx="7" cy="16.8" r="1.1" fill="#ffffff"/>
        </svg>
        <span>0438152906</span>
      </p>
    </section>

    <footer class="email-band">
      <span class="email-address">benedictrowlanpt@mailora.com.au</span>
    </footer>
  </main>
</body>
</html>
```